Crestwell Renewal Business Card Design Phase 2

Professional and clean design. The design colors should flow with the logo. Two-sided card with the website on the back which is:

www.CrestwellRenewal.example.

"Specializing in Water Damage Restoration"

On the front I need the name, email, phone, and logo.

Name: Dorian Halvek
Email: Dorian@CrestwellRenewal.example
Phone: 555-318-2046 for now

I only have the Preview and Thumbnail right now but should have the source files uploaded within a day or two.

Target Market(s)

Flood victims, home owners with water damage from busted pipes etc...

Industry/Entity Type

Business

Contact Information for Business Card

Name: Dorian Halvek

Font styles to use
Serif
Sans Serif

Requirements
Must have
• Business Card Details Info

```html
<!DOCTYPE html>
<html lang="en">
<head>
<meta charset="utf-8">
<title>Crestwell Renewal Business Cards</title>
<link href="https://fonts.googleapis.com/css2?family=Oswald:wght@500&family=Open+Sans:wght@400&family=Tinos&display=swap" rel="stylesheet">
<style>
  :root {
    --navy: #1d3a68;
    --green: #4b8a3b;
    --rule: #8a94a3;
    --card: #ffffff;
    --backdrop: #e9e6e1;
  }
  html, body {
    margin: 0;
    width: 1200px;
    height: 952px;
    overflow: hidden;
    background: var(--backdrop);
  }
  .canvas {
    position: relative;
    width: 1200px;
    height: 952px;
  }
  .card {
    position: absolute;
    width: 620px;
    height: 354px;
    background: var(--card);
    box-shadow: 0 6px 18px rgba(0,0,0,0.18);
    overflow: hidden;
  }
  .card--back { left: 70px; top: 60px; }
  .card--front { left: 510px; top: 530px; }
  .card__bands {
    position: absolute;
    inset: 0;
    width: 620px;
    height: 354px;
  }
  .wordmark {
    position: absolute;
    font-family: "Oswald", sans-serif;
    font-weight: 500;
    color: var(--navy);
    line-height: 1;
    letter-spacing: 0.5px;
    white-space: nowrap;
  }
  .card--back .wordmark {
    left: 84px;
    top: 70px;
    font-size: 64px;
  }
  .card--front .wordmark {
    left: 150px;
    top: 40px;
    font-size: 52px;
  }
  .tagline {
    position: absolute;
    left: 150px;
    top: 170px;
    font-family: "Tinos", serif;
    font-size: 17px;
    color: var(--navy);
    white-space: nowrap;
  }
  .website {
    position: absolute;
    right: 30px;
    top: 322px;
    font-family: "Open Sans", sans-serif;
    font-size: 14px;
    color: var(--navy);
  }
  .divider {
    position: absolute;
    left: 30px;
    right: 30px;
    top: 198px;
    height: 2px;
    background: var(--rule);
  }
  .contact {
    position: absolute;
    display: flex;
    align-items: center;
    gap: 10px;
    font-family: "Open Sans", sans-serif;
    white-space: nowrap;
  }
  .contact--name {
    left: 40px;
    top: 228px;
    font-size: 20px;
    color: var(--green);
  }
  .contact--phone {
    left: 330px;
    top: 230px;
    font-size: 15px;
    color: var(--navy);
  }
  .contact--email {
    left: 330px;
    top: 252px;
    font-size: 15px;
    color: var(--navy);
  }
  .icon { display: block; flex: none; }
</style>
</head>
<body>
<main class="canvas">

  <section class="card card--back" aria-label="Back of business card">
    <svg class="card__bands" viewBox="0 0 620 354" aria-hidden="true">
      <polygon points="0,318 300,318 285,354 0,354" fill="var(--navy)"/>
      <polygon points="300,296 620,296 620,354 268,354" fill="var(--green)"/>
      <polygon points="288,318 304,318 276,354 260,354" fill="var(--card)"/>
    </svg>
    <div class="wordmark">Crestwell Renewal</div>
    <div class="tagline">"Specializing in Water Damage Restoration"</div>
    <div class="website">www.CrestwellRenewal.example</div>
  </section>

  <section class="card card--front" aria-label="Front of business card">
    <svg class="card__bands" viewBox="0 0 620 354" aria-hidden="true">
      <polygon points="340,0 620,0 620,22 320,22" fill="var(--green)"/>
      <polygon points="360,0 620,0 620,14 352,14" fill="var(--navy)"/>
      <polygon points="0,300 300,300 285,330 0,330" fill="var(--navy)"/>
      <polygon points="290,330 620,330 620,285 300,285 262,354 620,354" fill="var(--green)"/>
      <polygon points="300,285 620,285 620,354 262,354" fill="var(--green)"/>
    </svg>
    <div class="wordmark">Crestwell Renewal</div>
    <div class="divider"></div>

    <div class="contact contact--name">
      <svg class="icon" width="24" height="24" viewBox="0 0 24 24" aria-hidden="true">
        <circle cx="12" cy="12" r="12" fill="var(--navy)"/>
        <circle cx="12" cy="9" r="4" fill="#fff"/>
        <path d="M5 19c1.5-4 12.5-4 14 0z" fill="#fff"/>
      </svg>
      <span>Dorian Halvek</span>
    </div>

    <div class="contact contact--phone">
      <svg class="icon" width="14" height="14" viewBox="0 0 14 14" aria-hidden="true">
        <circle cx="7" cy="7" r="7" fill="var(--green)"/>
        <path d="M4.5 3.5l1.3 1.6-.7 1c.5 1 1.1 1.6 2 2l1-.7 1.6 1.3-.8 1.2c-2.6-.3-4.8-2.5-5.1-5.1z" fill="#fff"/>
      </svg>
      <span>555-318-2046</span>
    </div>

    <div class="contact contact--email">
      <svg class="icon" width="14" height="10" viewBox="0 0 14 10" aria-hidden="true">
        <rect width="14" height="10" fill="var(--green)"/>
        <path d="M0 0l7 5.5L14 0" fill="none" stroke="#fff" stroke-width="1.2"/>
      </svg>
      <span>Dorian@CrestwellRenewal.example</span>
    </div>
  </section>

</main>
</body>
</html>
```